Landing Page IT Security Vendor

We need a landing page that uses our colour scheme (www.veldonguard.com). We created a draft (see attached). We do not need standard stock template design pages. Please only apply if you can design pages from scratch and try to be as close as possible to our draft. It is ok to also purchase commecrial stock pictures

Coding

Coded - Design and coding required

Number of Pages Required

1 page

```html
<!DOCTYPE html>
<html lang="en">
<head>
<meta charset="utf-8">
<title>Veldon Guard – Security Awareness Training</title>
<link href="https://fonts.googleapis.com/css2?family=Roboto:wght@300;400;500;700&family=Rubik:wght@400;500;600&display=swap" rel="stylesheet">
<style>
:root{
  --teal:#00b3b9;
  --teal-dark:#009ea4;
  --ice:#d8f1f5;
  --orange:#fbab1c;
  --orange-text:#f7a21a;
  --ink:#1d1d1d;
  --body:#454545;
  --grey-band:#8f8f8f;
  --card-border:#e0e0e0;
  --white:#ffffff;
}
*{margin:0;padding:0;box-sizing:border-box}
html,body{width:713px;height:1200px;overflow:hidden}
body{position:relative;font-family:'Roboto',sans-serif;background:var(--white);color:var(--ink)}
.abs{position:absolute}

/* hero */
.hero{left:0;top:0;width:713px;height:394px;background:var(--teal)}
.award-strip{left:18px;top:22px;width:570px;display:flex;gap:12px;color:var(--white);font-family:'Rubik',sans-serif;font-size:7.2px;line-height:10.5px}
.award{display:flex;align-items:center;gap:6px}
.award svg{flex:none}
.nav-home{left:592px;top:22px;width:50px;height:23px;border-radius:12px;background:#5fd4d6;color:#1f6f73;font-size:10px;display:flex;align-items:center;justify-content:center}
.nav-solution{left:651px;top:27px;color:var(--white);font-size:10px}
.doodles{left:290px;top:55px;width:290px;height:320px;background:radial-gradient(ellipse at center,rgba(255,255,255,.12),rgba(255,255,255,0) 70%)}
.portrait{left:560px;top:80px;width:153px;height:314px;background:linear-gradient(160deg,#d9844a 0%,#c9a48a 35%,#9aa3a7 70%,#7f8a8e 100%);border-radius:70px 0 0 0}
.kicker{left:19px;top:84px;color:var(--white);font-size:20px;font-weight:300;letter-spacing:.2px}
.headline{left:19px;top:134px;color:var(--white);font-size:31.5px;line-height:37.5px;font-weight:300;letter-spacing:.2px}
.demo-btn{left:412px;top:133px;width:152px;height:36px;border-radius:18px;background:#c9f4f6;color:#3f6d70;font-size:13px;display:flex;align-items:center;justify-content:center}
.help-title{left:108px;top:318px;color:var(--white);font-family:'Rubik',sans-serif;font-weight:600;font-size:19px}
.help-line{left:73px;top:341px;width:475px;border-top:1.5px dotted var(--white)}
.tick{width:0;height:17px;border-left:1.5px dotted var(--white);top:333px}

/* help section */
.help-bg{left:0;top:394px;width:713px;height:270px;background:linear-gradient(180deg,#c9eef3 0%,var(--ice) 60%,#e3f6f8 100%)}
.card{top:373px;width:197px;height:252px;background:var(--white);border:4px solid var(--card-border);padding:19px 4px 0 16px}
.card h3{font-family:'Rubik',sans-serif;font-weight:500;color:var(--orange-text);font-size:10.2px;line-height:15.5px;min-height:47px;margin-bottom:3px;letter-spacing:0}
.card h4{font-family:'Rubik',sans-serif;font-weight:500;color:var(--ink);font-size:10.3px;line-height:12.6px;margin-bottom:9px}
.card p{color:var(--body);font-size:9.2px;line-height:12.7px;font-weight:400}
.card .btn{position:absolute;left:18px;bottom:11px;width:154px;height:31px;border-radius:4px;background:var(--orange);color:var(--white);font-size:10.6px;display:flex;align-items:center;justify-content:center}

.mssp{left:0;top:664px;width:713px;height:46px;background:var(--grey-band);color:var(--white);font-family:'Rubik',sans-serif;font-weight:500;font-size:14px;display:flex;align-items:center;justify-content:center}
.mssp u{text-underline-offset:2px}

/* trust */
.trust-title{left:36px;top:733px;font-size:19px;line-height:25px;color:var(--ink)}
.trust-title span{color:var(--orange)}
.trust-copy{left:36px;top:795px;width:360px;font-size:11.5px;line-height:13.5px;color:var(--body);font-weight:300}
.trust-copy p{margin-bottom:13px}
.cta{left:36px;top:908px;width:344px;height:40px;border-radius:4px;background:var(--orange);color:var(--white);font-family:'Rubik',sans-serif;font-weight:500;font-size:10.5px;display:flex;align-items:center;justify-content:center}
.clients{left:433px;top:719px;width:250px;height:232px;background:var(--white);box-shadow:0 0 6px rgba(0,0,0,.07);border-radius:6px}
.client{position:absolute;font-family:'Rubik',sans-serif;font-weight:500;font-size:12px;color:#333;display:flex;align-items:center;gap:5px}
.client i{display:block;width:10px;height:10px;background:#e23a2e;flex:none}

/* footer */
.footer{left:0;top:995px;width:713px;height:205px;background:var(--teal)}
.f-head{color:var(--white);font-size:12px;font-weight:500}
.f-col{color:#e9fbfb;font-size:9.6px;line-height:15.2px}
.f-rule{left:0;top:1133px;width:713px;border-top:1px solid rgba(255,255,255,.55)}
.brand{left:4px;top:1159px;color:var(--white);font-family:'Rubik',sans-serif;font-weight:600;font-size:11px;display:flex;align-items:center;gap:4px}
.brand i{display:block;width:14px;height:14px;border-radius:50%;background:#f2b233}
.rights{left:3px;top:1185px;color:#dff6f6;font-size:8px}
.badges{left:186px;top:1156px;display:flex;gap:17px;align-items:center}
.badges span{display:block;width:30px;height:38px;border-radius:4px;background:rgba(255,255,255,.35)}
.badges span.round{border-radius:50%;height:38px;width:38px}
</style>
</head>
<body>

<section class="abs hero" aria-label="Hero">
  <div class="abs doodles" role="img" aria-label="Hand-drawn line doodles of charts, books, money signs and people"></div>
  <div class="abs portrait" role="img" aria-label="Photo of a smiling woman holding a tablet"></div>

  <div class="abs award-strip">
    <div class="award">
      <svg width="14" height="14" viewBox="0 0 14 14"><path d="M3 1h8v3a4 4 0 0 1-8 0zM1 2h2v2a2 2 0 0 1-2-2zM13 2h-2v2a2 2 0 0 0 2-2zM6 8h2v2h2v2H4v-2h2z" fill="#fff"/></svg>
      <span>In 2020, VELDON won the Cyber Defence<br>Excellence Award for Best "Anti Phishing"</span>
    </div>
    <div class="award">
      <svg width="20" height="20" viewBox="0 0 20 20"><circle cx="10" cy="10" r="8.5" fill="none" stroke="#fff" stroke-dasharray="2 1.5"/><path d="M10 5l1.5 3.2 3.4.4-2.5 2.3.7 3.4L10 12.6 6.9 14.3l.7-3.4-2.5-2.3 3.4-.4z" fill="#fff"/></svg>
      <span>In 2020, VELDON won the Cyber Defence Excellence<br>Award for Best "Security Education Platform"</span>
    </div>
    <div class="award">
      <svg width="20" height="20" viewBox="0 0 20 20"><circle cx="10" cy="10" r="8.5" fill="none" stroke="#fff" stroke-dasharray="2 1.5"/><text x="10" y="13.5" font-size="9" fill="#fff" text-anchor="middle" font-family="Roboto,sans-serif">1</text></svg>
      <span>2020 Gold Winner "Cyber Security Education<br>and Training" In the SecureWare Product guide</span>
    </div>
  </div>
  <div class="abs nav-home">Home</div>
  <div class="abs nav-solution">Solution ⌄</div>

  <p class="abs kicker">CYBER SECURITY STARTS WITH PEOPLE</p>
  <h1 class="abs headline">TRAIN YOUR STAFF WITH<br>VELDON AND IMPROVE CYBER<br>SECURITY AWARENESS</h1>
  <div class="abs demo-btn">Request a demo</div>

  <h2 class="abs help-title">HOW CAN WE HELP ?</h2>
  <div class="abs help-line"></div>
  <div class="abs tick" style="left:97px"></div>
  <div class="abs tick" style="left:353px"></div>
  <div class="abs tick" style="left:547px"></div>
</section>

<div class="abs help-bg"></div>

<article class="abs card" style="left:28px">
  <h3>IMPORT OUR TRAINING<br>COURSES IN YOUR LMS</h3>
  <h4>Buy out of the box or custom tailored security courses you can import in your elearning</h4>
  <p>VELDON offers 250 fully customizable training modules in +30 languages. Games, videos, exams, posters, offline, micro-training and much more!</p>
  <div class="btn">EXPLORE OUR TRAINING</div>
</article>
<article class="abs card" style="left:264px">
  <h3>LET US DEVELOP A SECURITY<br>AWARENESS PROGRAM</h3>
  <h4>VELDON Security will assist you in improving security awareness - with money back guarantee!</h4>
  <p>Our security awareness specialists will identify risky users via phishing simulations. We develop a tailored awareness program and reduce your exposure to social hacking.</p>
  <div class="btn">EXPLORE OUR SERVICES</div>
</article>
<article class="abs card" style="left:500px">
  <h3>INSTALL THE VELDON SOFTWARE<br>ON-PREMISE OR GET ACCESS<br>TO THE SAAS VERSION</h3>
  <h4>You want to run the campaign yourself? Choose your preferred setup type and get started in 24h!</h4>
  <p>The VELDON Software can be installed on-premise or in the cloud. If you don't want to deal with the installation we onboard you in 24h on our SaaS!</p>
  <div class="btn">EXPLORE OUR SOFTWARE</div>
</article>

<div class="abs mssp">VELDON is also available for MSSP -&nbsp;<u>learn more</u></div>

<h2 class="abs trust-title" style="font-weight:400">Already over <span>12'000'000</span><br>Employees worldwide trust and use VELDON.</h2>
<div class="abs trust-copy">
  <p>Veldon Guard is a name you can trust! Because we have won countless awards since 2015 and help well-known brands around the world.</p>
  <p>You know you're getting a quality solution with us.</p>
  <p>Our Services can be customized to fit your needs and company size. Talk to our team today to learn more.</p>
</div>
<div class="abs cta">GET IN CONTACT WITH THE VELDON TEAM NOW !</div>

<div class="abs clients" aria-label="Client names">
  <div class="client" style="left:14px;top:32px"><i style="background:#1b3a8f"></i>Arvena</div>
  <div class="client" style="left:92px;top:32px"><i></i>Railo</div>
  <div class="client" style="left:165px;top:32px"><i></i>Casamo</div>
  <div class="client" style="left:26px;top:92px"><i></i>Brennwerk</div>
  <div class="client" style="left:128px;top:92px"><i style="background:#1b3a8f"></i>Altavia</div>
  <div class="client" style="left:14px;top:140px"><i style="background:#0a8a73"></i>Mühlental</div>
  <div class="client" style="left:128px;top:140px">Kessler Informatik</div>
  <div class="client" style="left:14px;top:196px">Lumachem</div>
  <div class="client" style="left:128px;top:190px;font-weight:400;line-height:13px">Stadtwerk<br>Nordhain</div>
</div>

<footer class="abs footer">
  <div class="abs f-head" style="left:36px;top:26px">CONTACTS</div>
  <div class="abs f-head" style="left:613px;top:26px">LANGUAGE</div>
  <div class="abs f-col" style="left:36px;top:52px">Address: Europe<br>Veldon Guard AG<br>Talweg 18 | 6301 Seeburg | Switzerland</div>
  <div class="abs f-col" style="left:267px;top:52px">Address: North America<br>Veldon Guard USA<br>4410 Orchard Park Dr<br>Suite 210<br>Riverton, TX 78599</div>
  <div class="abs f-col" style="left:426px;top:52px">Phone Global: +41 44 000 12 34<br>Phone USA: +1-555-010-2200<br>Phone USA Support: +1-555-010-2214<br>Phone France: +33 600 000 412<br>Phone UK: +44 (0) 7700 900123</div>
  <div class="abs f-col" style="left:613px;top:52px;font-size:10px;font-weight:500">English &nbsp;▾</div>
</footer>
<div class="abs f-rule"></div>
<div class="abs brand"><i></i>Veldon</div>
<div class="abs rights">All Rights Reserved 2020</div>
<div class="abs badges" aria-label="Award badges">
  <span></span><span class="round"></span><span></span><span></span><span></span><span style="width:44px;height:22px"></span><span></span><span></span><span style="width:60px;height:26px;border-radius:13px"></span><span class="round"></span>
</div>

</body>
</html>
```